Geschäftspapiere für Bauunternehmen
Zielgruppe
Wir sind ein Bauunternehmen.
Aufgabenstellung
Bitte das Briefpapier alles nötige für eine Angebotserstellung sowie Rechnungsstellung hinzufügen. Heißt: Logo, Firma, Firmensitz, Telefonnummer, Steuernummer und Bankdaten. Bankdaten: DE41 5108 0060 2294 7731 08 BIC: RQTNDEM1XXX

```html
<!DOCTYPE html>
<html lang="de">
<head>
<meta charset="utf-8">
<title>Brendel Bau – Briefpapier</title>
<link href="https://fonts.googleapis.com/css2?family=Montserrat:wght@400;500;600&display=swap" rel="stylesheet">
<style>
  :root {
    --ink: #111111;
    --red: #e30000;
    --red-dark: #120000;
    --paper: #ffffff;
    --band-dark: #101010;
  }
  * { margin: 0; padding: 0; box-sizing: border-box; }
  html, body { width: 949px; height: 1200px; overflow: hidden; background: var(--paper); }
  .letterhead {
    position: relative;
    width: 949px;
    height: 1200px;
    background: var(--paper);
    font-family: "Montserrat", sans-serif;
    color: var(--ink);
  }
  .top-band { position: absolute; top: 0; left: 0; width: 949px; height: 24px; display: block; }
  .bottom-band { position: absolute; bottom: 0; left: 0; width: 949px; height: 30px; display: block; }

  .brand {
    position: absolute;
    left: 100px;
    top: 286px;
    display: flex;
    align-items: center;
    gap: 14px;
  }
  .brand-square { width: 34px; height: 34px; background: var(--red); }
  .brand-name {
    font-size: 34px;
    font-weight: 400;
    letter-spacing: 0.5px;
    color: var(--ink);
  }

  .sender {
    position: absolute;
    left: 587px;
    top: 190px;
  }
  .sender-name { font-size: 27px; font-weight: 600; letter-spacing: 0.5px; line-height: 1.2; }
  .sender-address { margin-top: 4px; margin-left: 4px; font-size: 15px; line-height: 17px; }

  .contact-row, .bank-row {
    position: absolute;
    display: flex;
    align-items: center;
    font-size: 15px;
  }
  .contact-row { top: 1064px; left: 58px; }
  .bank-row { top: 1118px; left: 183px; }
  .contact-item { display: flex; align-items: center; gap: 14px; }
  .contact-item svg { width: 24px; height: 24px; fill: var(--ink); flex: none; }
  .contact-web { width: 296px; }
  .contact-phone { width: 262px; }
  .bank-iban { width: 375px; }
</style>
</head>
<body>
<main class="letterhead">

  <svg class="top-band" viewBox="0 0 949 24" preserveAspectRatio="none" aria-hidden="true">
    <defs>
      <linearGradient id="topGradient" x1="0" x2="1" y1="0" y2="0">
        <stop offset="0" stop-color="#120000"/>
        <stop offset="1" stop-color="#e30000"/>
      </linearGradient>
    </defs>
    <rect width="949" height="24" fill="url(#topGradient)"/>
    <polygon points="738,0 750,0 734,24 722,24" fill="#fff"/>
    <polygon points="772,0 786,0 770,24 756,24" fill="#fff"/>
  </svg>

  <div class="brand">
    <span class="brand-square"></span>
    <span class="brand-name">BRENDEL BAU</span>
  </div>

  <section class="sender">
    <h1 class="sender-name">Brendel Bau</h1>
    <p class="sender-address">Lindenhofer Weg 42,<br>12407 Berlin, Germany</p>
  </section>

  <div class="contact-row">
    <div class="contact-item contact-web">
      <svg viewBox="0 0 24 24" aria-hidden="true"><circle cx="12" cy="12" r="10.5" fill="none" stroke="#111" stroke-width="2"/><path d="M6 6c2 1 3 3 2 5s1 3 2 5l-1 4c-3-1-6-5-5-9zM13 4c2 0 3 2 5 2 1 2 2 4 1 6-2 0-3-2-5-1s0 4-2 5c-1-2-2-4-1-6s2-3 2-6z"/></svg>
      <span>www.brendel-bau.de</span>
    </div>
    <div class="contact-item contact-phone">
      <svg viewBox="0 0 24 24" aria-hidden="true"><path d="M6.6 2.5l3 3.7c.5.6.4 1.4-.1 1.9L8 9.6c1 2.6 3.7 5.3 6.4 6.4l1.5-1.5c.5-.5 1.3-.6 1.9-.1l3.7 3c.6.5.6 1.4.1 2l-1.8 1.8c-1 1-2.6 1.2-3.8.5C10 18.8 5.2 14 2.3 8c-.7-1.2-.5-2.8.5-3.8l1.8-1.8c.6-.5 1.5-.5 2 .1z"/></svg>
      <span>030 517 62 418</span>
    </div>
    <div class="contact-item">
      <svg viewBox="0 0 24 24" aria-hidden="true"><path d="M0 5h24v14H0z"/><path d="M1 6l11 8 11-8M1 18l8-6M23 18l-8-6" fill="none" stroke="#fff" stroke-width="1.6"/></svg>
      <span>info@brendel-bau.de</span>
    </div>
  </div>

  <div class="bank-row">
    <div class="contact-item bank-iban">
      <svg viewBox="0 0 24 24" aria-hidden="true"><path d="M12 1l11 6H1z"/><rect x="2" y="8" width="20" height="2"/><rect x="4" y="11" width="2.4" height="8"/><rect x="8.5" y="11" width="2.4" height="8"/><rect x="13" y="11" width="2.4" height="8"/><rect x="17.6" y="11" width="2.4" height="8"/><rect x="1" y="20" width="22" height="3"/></svg>
      <span>DE41 5108 0060 2294 7731 08</span>
    </div>
    <span>BIC: RQTNDEM1XXX</span>
  </div>

  <svg class="bottom-band" viewBox="0 0 949 30" preserveAspectRatio="none" aria-hidden="true">
    <rect width="949" height="30" fill="#101010"/>
    <polygon points="140,0 152,0 134,30 122,30" fill="#fff"/>
    <polygon points="172,0 186,0 168,30 154,30" fill="#fff"/>
  </svg>

</main>
</body>
</html>
```